I am a surgeon that operates on gynaecological cancer. Wish a design and logo for letter head.

Design should include my name: Dr. Kiran Mudaly, qualifications: FTELSWOB, CGO. and state that I am a Gynaecological Oncologist and Advanced Laparoscopic Surgeon.
As for a logo. As all cancer is related to DNA, I think that that double helix could be used to symbolise a female shape, exaggerating the abdomen to suggest a mass.

Reason: Extended to view changes I have asked for.

```html
<!DOCTYPE html>
<html lang="en">
<head>
<meta charset="utf-8">
<title>Dr. Kiran Mudaly – Letterhead</title>
<link rel="stylesheet" href="https://fonts.googleapis.com/css2?family=Source+Sans+3:ital,wght@0,700;1,700&display=swap">
<style>
  :root {
    --paper: #ffffff;
    --teal: #13897c;
    --rule-red: #c92f2a;
    --sky: #1f8fcf;
    --leaf-light: #d7f5d4;
    --leaf-mid: #9fe39a;
  }
  * { margin: 0; padding: 0; box-sizing: border-box; }
  html, body {
    width: 927px;
    height: 1200px;
    overflow: hidden;
    background: var(--paper);
  }
  .letterhead {
    position: relative;
    width: 927px;
    height: 1200px;
    background: var(--paper);
    font-family: "Source Sans 3", "Myriad Pro", Arial, sans-serif;
  }
  .header-rule {
    position: absolute;
    left: 0;
    top: 119px;
    width: 927px;
    height: 4px;
    background: var(--rule-red);
  }
  .brand-mark {
    position: absolute;
    left: 84px;
    top: 68px;
    width: 90px;
    height: 142px;
    display: flex;
    flex-direction: column;
    align-items: center;
    justify-content: center;
    gap: 10px;
    color: var(--teal);
    font-weight: 700;
    font-size: 17px;
    line-height: 1.05;
    text-align: center;
    background: var(--paper);
    z-index: 2;
  }
  .brand-mark .dot {
    width: 50px;
    height: 50px;
    border-radius: 50%;
    background: var(--leaf-mid);
  }
  .doctor-name {
    position: absolute;
    left: 217px;
    top: 76px;
    color: var(--teal);
    font-weight: 700;
    font-size: 38px;
    line-height: 1;
    font-variant: small-caps;
    letter-spacing: -0.6px;
    white-space: nowrap;
  }
  .doctor-name .credentials {
    font-style: italic;
    font-variant: normal;
    font-size: 28px;
    letter-spacing: -0.8px;
  }
  .specialty {
    position: absolute;
    left: 276px;
    top: 133px;
    color: var(--sky);
    font-style: italic;
    font-weight: 700;
    font-size: 18px;
    line-height: 1.1;
    letter-spacing: -0.7px;
    white-space: nowrap;
  }
  .corner-motif {
    position: absolute;
    right: 0;
    bottom: 0;
    width: 300px;
    height: 236px;
    background: radial-gradient(ellipse at 65% 55%, var(--leaf-mid) 0%, var(--leaf-light) 55%, rgba(215,245,212,0) 80%);
  }
</style>
</head>
<body>
  <main class="letterhead">
    <div class="header-rule"></div>
    <div class="brand-mark">
      <span class="dot"></span>
      <span>Kiran<br>Mudaly</span>
    </div>
    <h1 class="doctor-name">Dr. Kiran Mudaly, <span class="credentials">FTELSWOB, CGO</span></h1>
    <p class="specialty">Gynaecological Oncologist and Advanced Laparoscopic Surgeon</p>
    <div class="corner-motif" role="img" aria-label="Soft green butterfly illustration in the lower right corner"></div>
  </main>
</body>
</html>
```